Marlowick Investment Partners Website | ||
Financial Services | ||
mipfundexample.com | ||
The company is an investment fund. The site must inspire trust and confidence yet have style. It must be VERY professional. | ||
I like things simple and elegant. Rich and classy in appearance. I don't care too much about colors, but it's probably easiest to use the colors already used in my logos. | ||
Clean/Simple Professional Content Driven Conservative Sophisticated Corporate Modern Elegant Traditional Masculine |
left side | ||
https://www.castrelfunds.example/cm/Satellite?pagename=cfVanityWrapper&UserFriendlyURL=home | ||
http://www.tuvrelle.example/ | ||
http://www2.pinegate.example/US/individual-investors | ||
The site doesn't need to be terribly complex nor work as a stand-alone source for sales. It is mainly a source for further information for people I have talked to about the fund personally. It should also be a place for current clients to check on performance of their portfolios. Of the websites listed above: I like Castrel Banks's appearance I like Tuvrelle's layout and simplicity pinegate I like in general I also made a mock up of how i saw the site, which I'll upload once the contest is up and running. |

```html
<!DOCTYPE html>
<html lang="en">
<head>
<meta charset="utf-8">
<title>Marlowick Investment Partners — Company</title>
<link rel="stylesheet" href="https://fonts.googleapis.com/css2?family=Open+Sans:wght@400;600;700&family=Lora:ital@1&display=swap">
<style>
  :root {
    --stage: #e6e6e6;
    --page: #ffffff;
    --teal: #1a8fa8;
    --teal-dark: #137489;
    --bar: #ececec;
    --client-bg: #d3cfc8;
    --header-dark: #1b1b1b;
    --header-mid: #3a3a3a;
    --brand-text: #e4e4e4;
    --text: #333333;
    --muted: #555555;
    --footer: #ebebeb;
  }
  * { box-sizing: border-box; margin: 0; padding: 0; }
  html, body { width: 1200px; height: 901px; overflow: hidden; }
  body { background: var(--stage); font-family: "Open Sans", Arial, sans-serif; color: var(--text); position: relative; }

  .site { position: absolute; left: 127px; top: 85px; width: 944px; height: 733px; background: var(--page); box-shadow: 0 3px 10px rgba(0,0,0,.25); }

  .access-bar { position: absolute; left: 0; top: 0; width: 944px; height: 42px; background: var(--bar); display: flex; align-items: center; }
  .access-bar .accent { width: 165px; height: 42px; background: var(--teal); }
  .access-bar .client { width: 127px; height: 42px; background: var(--client-bg); color: #fff; font-size: 15px; display: flex; align-items: center; justify-content: center; }
  .login { display: flex; align-items: center; gap: 8px; font-size: 13px; color: var(--muted); margin-left: 12px; }
  .login input { width: 118px; height: 20px; border: 1px solid #c9c9c9; background: #fff; }
  .login .pw-label { margin-left: 10px; }
  .login .go { background: #4a4a4a; color: #fff; font-size: 11px; font-weight: 700; padding: 3px 6px; margin-left: 4px; }
  .forgot { font-size: 10px; line-height: 13px; color: #888; margin-left: 18px; }

  .masthead { position: absolute; left: 0; top: 42px; width: 944px; height: 190px; background: radial-gradient(ellipse at 78% 40%, var(--header-mid), var(--header-dark) 70%); }
  .brand { position: absolute; left: 36px; top: 70px; display: flex; align-items: center; gap: 16px; }
  .brand-square { width: 40px; height: 40px; background: var(--teal); }
  .brand-name { font-family: "Open Sans", Arial, sans-serif; font-weight: 600; font-size: 26px; color: var(--brand-text); }
  .tagline { position: absolute; right: 42px; top: 130px; width: 340px; font-family: "Lora", Georgia, serif; font-style: italic; font-size: 14px; line-height: 19px; color: #d8d8d8; }

  .side-nav { position: absolute; left: 0; top: 232px; width: 165px; height: 452px; background: var(--teal); padding-top: 22px; }
  .side-nav a { display: block; height: 36px; line-height: 36px; padding-left: 14px; color: #fff; font-size: 14px; font-weight: 600; text-decoration: none; border-bottom: 1px solid var(--teal-dark); }

  .side-art { position: absolute; left: 165px; top: 232px; width: 134px; height: 452px; background: linear-gradient(180deg, #e9e6e1 0%, #d8d3cb 60%, #c9c3b9 100%); }

  .content { position: absolute; left: 331px; top: 262px; width: 536px; }
  .content h1 { font-size: 22px; font-weight: 400; color: #222; padding-bottom: 6px; border-bottom: 1px solid #999; margin-bottom: 26px; }
  .content p { font-size: 13.5px; line-height: 23px; color: var(--text); }

  .site-footer { position: absolute; left: 0; top: 684px; width: 944px; height: 49px; background: var(--footer); font-size: 11px; color: #444; display: flex; align-items: center; justify-content: flex-end; padding-right: 28px; }
</style>
</head>
<body>
  <div class="site">
    <div class="access-bar">
      <div class="accent"></div>
      <div class="client">Client Access</div>
      <form class="login">
        <label>User Name:</label><input type="text">
        <label class="pw-label">Password:</label><input type="password">
        <span class="go">GO</span>
      </form>
      <div class="forgot">Forgot your password?<br>Reset it here.</div>
    </div>

    <header class="masthead">
      <div class="brand">
        <div class="brand-square"></div>
        <div class="brand-name">Marlowick Investment Partners</div>
      </div>
      <p class="tagline">"You can get everything you want in life, if you just help enough other people get what they want."</p>
    </header>

    <nav class="side-nav">
      <a href="#">Company</a>
      <a href="#">Philosophy</a>
      <a href="#">Limited Partners</a>
      <a href="#">Strategies</a>
      <a href="#">MarLoWick Capital</a>
      <a href="#">Articles</a>
      <a href="#">Contact</a>
    </nav>

    <div class="side-art" role="img" aria-label="Faint bull and bear market illustration in soft beige tones"></div>

    <main class="content">
      <h1>Company</h1>
      <p>Marlowick Investment Partners (MIP) is a company founded on the simple premise that "You can get everything you want in life, if you just help enough other people get what they want." Our goal, therefore, is to provide safe, consistent, market beating returns while charging fees much lower than our hedge fund peers. MIP has also gone to great length to bring the advantages of hedge fund strategies and the intelligent employment of leverage to groups that have traditionally been excluded from participation in hedge fund strategies. Rather than seeking a few huge investors up front and trying to "get rich quick" we therefore prefer to have many small investors and grow the business by letting our performance speak for itself in the long term.</p>
    </main>

    <footer class="site-footer">Copyright © 2011 Marlowick Investment Partners</footer>
  </div>
</body>
</html>
```